We need a business card design for a new company based in
Perth, Western Australia called Bexom Tiling Services. We specialize in laying Wall and Floor Tiles and Stone. We expertise in all small to large format tiles and do good quality work. Sincerity and Convition is what seperates us from others.

```html
<!DOCTYPE html>
<html lang="en">
<head>
<meta charset="utf-8">
<title>Bexom Tiling Services – Business Card</title>
<link rel="stylesheet" href="https://fonts.googleapis.com/css2?family=Open+Sans:wght@400;600&display=swap">
<style>
  :root {
    --stage: #7a7a7a;
    --card: #121212;
    --tile: #1d1d1d;
    --tile-edge: #0c0c0c;
    --text-light: #e6e6e6;
    --text-mid: #8d8d8d;
    --text-dim: #4a4a4a;
    --icon-bg: #d8d8d8;
  }
  * { box-sizing: border-box; margin: 0; padding: 0; }
  html, body { width: 1200px; height: 775px; overflow: hidden; }
  body {
    background: var(--stage);
    font-family: "Open Sans", Arial, sans-serif;
    position: relative;
  }
  .card {
    position: absolute;
    top: 230px;
    width: 540px;
    height: 312px;
    background: var(--card);
    overflow: hidden;
    box-shadow: 0 10px 24px rgba(0,0,0,0.35);
  }
  .card--front { left: 30px; }
  .card--back { left: 630px; }
  .tile-corner { position: absolute; left: 0; top: 0; width: 170px; height: 312px; }

  .brand-name {
    font-family: "Open Sans", Arial, sans-serif;
    font-weight: 600;
    color: var(--text-light);
    text-transform: uppercase;
    letter-spacing: 0.08em;
    white-space: nowrap;
  }
  .card--front .brand-name {
    position: absolute; left: 0; right: 0; top: 136px;
    text-align: center; font-size: 24px;
  }
  .card--front .website {
    position: absolute; left: 150px; top: 250px;
    font-size: 11px; letter-spacing: 0.18em; color: var(--text-dim);
  }

  .contact-block {
    position: absolute; right: 30px; top: 92px;
    text-align: right;
  }
  .card--back .brand-name { font-size: 15px; margin-bottom: 18px; }
  .person-name { font-size: 13px; font-weight: 600; color: var(--text-light); }
  .person-role { font-size: 12px; color: var(--text-mid); margin-bottom: 12px; }
  .contact-line {
    display: flex; justify-content: flex-end; align-items: center; gap: 10px;
    font-size: 12px; color: var(--text-mid); line-height: 22px;
  }
  .contact-icon { width: 14px; height: 14px; }
  .address { font-size: 12px; color: var(--text-mid); margin-top: 14px; margin-right: 24px; line-height: 17px; }
</style>
</head>
<body>

<section class="card card--front" aria-label="Card front">
  <svg class="tile-corner" viewBox="0 0 170 312" role="img" aria-label="Diagonal tile pattern in dark grey">
    <polygon points="60,0 170,0 60,230 0,300 0,120" fill="var(--tile)"/>
  </svg>
  <p class="brand-name">Bexom Tiling Services</p>
  <p class="website">www.bexomtiling.com</p>
</section>

<section class="card card--back" aria-label="Card back">
  <svg class="tile-corner" viewBox="0 0 170 312" role="img" aria-label="Diagonal tile pattern in dark grey">
    <polygon points="60,0 170,0 60,230 0,300 0,120" fill="var(--tile)"/>
  </svg>
  <div class="contact-block">
    <p class="brand-name">Bexom Tiling Services</p>
    <p class="person-name">Daniel Prescott</p>
    <p class="person-role">President</p>
    <p class="contact-line">+61 4120 55318
      <svg class="contact-icon" viewBox="0 0 14 14" aria-hidden="true">
        <rect width="14" height="14" rx="2" fill="var(--icon-bg)"/>
        <path d="M5 3 L7 5 L6 6.5 Q7 8 8 8.5 L9.5 7.5 L11 9.5 Q9.5 11 8 10.8 Q4 9.5 3.2 5.5 Q3.2 4 5 3 Z" fill="var(--card)"/>
      </svg>
    </p>
    <p class="contact-line">+61 892 470 116
      <svg class="contact-icon" viewBox="0 0 14 14" aria-hidden="true">
        <rect width="14" height="14" rx="2" fill="var(--icon-bg)"/>
        <path d="M2.5 6 Q7 2.5 11.5 6 L10.5 7.5 L9 6.5 L9 5.5 Q7 4.8 5 5.5 L5 6.5 L3.5 7.5 Z" fill="var(--card)"/>
        <rect x="4" y="8" width="6" height="3" fill="var(--card)"/>
      </svg>
    </p>
    <p class="contact-line">info@bexomtiling.com
      <svg class="contact-icon" viewBox="0 0 14 14" aria-hidden="true">
        <rect width="14" height="14" rx="2" fill="var(--icon-bg)"/>
        <rect x="2.5" y="4" width="9" height="6.5" fill="none" stroke="var(--card)" stroke-width="1"/>
        <path d="M2.5 4 L7 8 L11.5 4" fill="none" stroke="var(--card)" stroke-width="1"/>
      </svg>
    </p>
    <p class="address">27 Kestrel Bay Road<br>Perth, WA 6000</p>
  </div>
</section>

</body>
</html>
```